Upgrade my Web to PHP format

I need move my web site http://qrnlivo7.example to PHP format my hosting is running under Linux with MySQL , all information is on old Web site and we need move to the new Web Design , We would like to see designs that use the color of our logo.

The final design should communicate about security software , security services and hosting Vorlan Stride k server.

Is very important easy installation and instructions of installation.

Target Market(s)

Bank and security company

Industry/Entity Type

Computer Security

Number of Pages Required

5+ page

Font styles to use
Sans Serif
Other font styles liked:
• arial, verdana.

Colors
3276b5
33a6d7
85cae6
85acd3
88d0c7

Requirements
Must have
• respect to our colors and all link to all pages, videos , and PDF.
Nice to have
• I would like design about security server and services , developer software security.
Should not have
• Anti Virus

```html
<!DOCTYPE html>
<html lang="en">
<head>
<meta charset="utf-8">
<title>Halvern Tech — Professional IT Services &amp; Support</title>
<link href="https://fonts.googleapis.com/css2?family=Open+Sans:wght@400;600;700;800&display=swap" rel="stylesheet">
<style>
:root{
  --brand:#3276b5;
  --sky:#33a6d7;
  --pale:#85cae6;
  --mist:#85acd3;
  --mint:#88d0c7;
  --navy:#0a53a4;
  --ink:#3c3c3c;
  --grey:#6d6d6d;
  --topbar:#eef7fb;
}
*{box-sizing:border-box;margin:0;padding:0}
html,body{width:713px;height:1200px;overflow:hidden}
body{font-family:"Open Sans",Arial,sans-serif;color:var(--ink);background:#fff;position:relative}
a{text-decoration:none;color:inherit}

.topbar{height:16px;background:var(--topbar);display:flex;align-items:center;padding:0 110px;gap:14px;font-size:4.6px;color:var(--grey)}
.topbar .item{display:flex;align-items:center;gap:3px}
.topbar svg{width:5px;height:5px;fill:var(--mist)}

.nav{height:35px;display:flex;align-items:center;padding:0 110px;justify-content:space-between;border-bottom:1px solid #e6eef5}
.brand{display:flex;align-items:center;gap:6px;font-weight:600;font-size:12px;color:#2a2a2a}
.brand .mark{width:10px;height:10px;background:var(--brand)}
.menu{display:flex;align-items:center;gap:13px;font-size:5.6px;font-weight:600;color:var(--sky)}
.menu .active{color:var(--brand)}
.menu .cta{background:var(--mint);color:#fff;padding:4px 24px;border-radius:8px}

.hero{height:299px;background:linear-gradient(90deg,#33a0d7,#2f86cb);position:relative;color:#fff}
.hero h1{position:absolute;left:108px;top:72px;font-size:22px;font-weight:700;line-height:27px;letter-spacing:.3px}
.hero p{position:absolute;left:109px;top:135px;width:260px;font-size:6.3px;line-height:10.5px}
.hero .more{position:absolute;left:110px;top:184px;width:85px;height:23px;border:1.5px solid rgba(255,255,255,.55);font-size:6.5px;font-weight:600;letter-spacing:.6px;color:rgba(255,255,255,.75);display:flex;align-items:center;justify-content:center}
.hero .art{position:absolute;left:400px;top:38px;width:265px;height:245px;border-radius:10px;background:radial-gradient(circle at 60% 50%,rgba(255,255,255,.35),rgba(255,255,255,.06) 70%)}

.services{height:228px;display:flex;padding:0 110px;padding-top:58px;gap:40px}
.services h2{font-size:16px;font-weight:700;color:var(--brand);margin-bottom:22px}
.integrated{width:233px}
.list{display:grid;grid-template-columns:127px 100px;row-gap:6px;font-size:8px;font-weight:600;color:#333}
.list li{list-style:none;display:flex;align-items:center;gap:6px}
.list li::before{content:"";width:7px;height:7px;border-radius:50%;background:var(--pale)}
.customer p{font-size:8px;line-height:13.4px;color:#444;width:240px}

.principles{height:214px;display:flex}
.principles .scene{width:350px;background:#f4f4f4;display:flex;align-items:center;justify-content:center}
.principles .scene div{width:260px;height:150px;border-radius:8px;background:linear-gradient(180deg,#e6e6e6,#dcdcdc)}
.principles .copy{flex:1;background:var(--navy);color:#fff;padding:30px 40px 0 41px}
.principles h3{font-size:13.5px;font-weight:700;line-height:20px;margin-bottom:12px}
.principles p{font-size:5.4px;line-height:9.3px;width:180px;margin-bottom:9px}
.principles .link{display:block;font-size:5.4px;line-height:9px;font-weight:700;margin-top:-2px}

.clients{height:267px;text-align:center;padding-top:50px}
.clients h2{font-size:16px;font-weight:700;color:var(--brand);margin-bottom:33px}
.logos{display:grid;padding:0 108px}
.logos.row1{grid-template-columns:repeat(5,1fr)}
.logos.row2{grid-template-columns:repeat(4,1fr);margin-top:36px}
.client{display:flex;align-items:center;justify-content:center;gap:4px;font-size:9.5px;font-weight:700;color:#555;height:34px}
.client i{width:8px;height:8px;background:#777;border-radius:50%}

.callout{height:85px;background:var(--navy);color:#fff;text-align:center;padding-top:16px}
.callout p{font-size:8.4px;margin-bottom:12px}
.callout a{display:inline-block;width:182px;height:31px;line-height:31px;background:var(--sky);font-size:11px;font-weight:700;letter-spacing:.6px}

.footer{height:57px;display:flex;align-items:center;justify-content:space-between;padding:0 110px;font-size:5.2px}
.footer .copy{font-weight:600;color:#555}
.footer nav{display:flex;gap:11px;font-weight:600;color:var(--sky)}
</style>
</head>
<body>

<header>
  <div class="topbar">
    <span class="item"><svg viewBox="0 0 10 10"><path d="M2 0l2 2-1 2 3 3 2-1 2 2-2 2C4 10 0 6 0 2z"/></svg>+1 (555) 0140 / +1 (555) 0141</span>
    <span class="item"><svg viewBox="0 0 10 10"><path d="M0 2h10v6H0z"/></svg>contact@halverntech.example</span>
    <span class="item"><svg viewBox="0 0 10 10"><path d="M1 10V3h3V0h5v10z"/></svg>120 Harbor Lane Suite 40 PORTVALE, 00000</span>
  </div>
  <div class="nav">
    <a class="brand" href="http://qrnlivo7.example"><span class="mark"></span>Halvern Tech</a>
    <nav class="menu">
      <a class="active" href="#">HOME</a>
      <a href="#">ABOUT</a>
      <a href="#">PRODUCTS</a>
      <a href="#">CLOUD SERVICES</a>
      <a href="#">SUPPORT</a>
      <a class="cta" href="#">CONTACT</a>
    </nav>
  </div>
</header>

<section class="hero">
  <h1>THE IDEAL PROFESSIONAL<br>IT SERVICES &amp; SUPPORT.</h1>
  <p>Our certified IT technicians and computer engineers excel with design, deployment, and maintaining communications systems. From implementing new data management systems to upgrading security standards, we can handle all your IT needs.</p>
  <a class="more" href="#">READ MORE</a>
  <div class="art" role="img" aria-label="Illustration of a server stack connected to screens, cloud, mail and wifi icons over a world map"></div>
</section>

<section class="services">
  <div class="integrated">
    <h2>INTEGRATED SERVICES</h2>
    <ul class="list">
      <li>Project Consulting</li><li>Network Design</li>
      <li>Security Solutions</li><li>Capacity Planning</li>
      <li>Security Assessments</li><li>Equipment Upgrades.</li>
      <li>Implementation</li>
    </ul>
  </div>
  <div class="customer">
    <h2>CUSTOMER SERVICES</h2>
    <p>Reliability and convenience are two parts of our customer services commitment. Our team is available 24 hours a day to provide continual monitoring and support. Remote and on-site services ensure you receive optimal service.</p>
  </div>
</section>

<section class="principles">
  <div class="scene"><div role="img" aria-label="Illustration of three colleagues meeting at a desk with laptops and a chart board"></div></div>
  <div class="copy">
    <h3>Effective Operating<br>Principles.</h3>
    <p>We are a company with extensive experience in the area of information technology for environments Vorlan Stride k (VS/200), and we are part of the Vorlan Partner Network.</p>
    <p>Our strength lies in the extensive knowledge and experience in the area of computer security and support in providing the best solutions, which cover the requirements of confidentiality and availability of data on that platform.</p>
    <a class="link" href="#">read more</a>
  </div>
</section>

<section class="clients">
  <h2>OUR SATISFIED CLIENTS</h2>
  <div class="logos row1">
    <div class="client"><i></i>Norvia Bank</div>
    <div class="client">Bancorsa</div>
    <div class="client">Ulterio</div>
    <div class="client">Banco Marenta N.V</div>
    <div class="client">Credimar C.A.</div>
  </div>
  <div class="logos row2">
    <div class="client"><i></i>Valdesco</div>
    <div class="client">KEL Bank</div>
    <div class="client">Trevo Coast Branch</div>
    <div class="client">Pelancom</div>
  </div>
</section>

<section class="callout">
  <p>Lorem ipsum dolor sit amet, consectetur adipiscing elit.</p>
  <a href="#">CONTACT US NOW!</a>
</section>

<footer class="footer">
  <span class="copy">Copyright 2015. Halvern Tech</span>
  <nav>
    <a href="#">HOME</a><a href="#">ABOUT</a><a href="#">PRODUCTS</a><a href="#">CLOUD SERVICES</a><a href="#">SUPPORT</a><a href="#">CONTACT US</a>
  </nav>
</footer>

</body>
</html>
```